Purchasing Management Consulting B to B Web Design PAYMENT GUARANTY

We'd like to build a new digital image for our website.

Our company is managing purchasing consultancy services for Large and Medium companies around 4 activities :
- Procurement outsourcing
- Purchasing consulting (cost reduction)
- Supply chain training
- Web platform to manage Supplier risk (TrovaNorm.com)

We now aim to harmonies our website in term of design in order to build a strongest Corporate Image.

SEE REQUIREMENT ENCLOSED

Please have a look on our current websites:
- www.kelpstrand.com
- www.qtr-network.com
- www.trovanorm.com

Reason: Hello, Some project received are not really professional and need more details. I did not see all deliverable requested in specifications. I'll revert to designer to improve design. Regards, Gaspard

Reason: Only few designers reply and feedback still need to be done.

Target Market(s)

Our business is exclusively Business to Business toward Medium and Large companies.

Industry/Entity Type

Digital

Requirements
Must have
• Website will be developped in Joomla CMS.
The user community will use Jomsocial module : Visitor should be "influenced" to communicate its contact details by registering the community.

Ergonomy, Simplicity and professionnalism is the key objectives.

Deliverables :
- Corporate Home page including clear access to our 4 activities
- Dynamique banner
- Corporate article / contact pages (1 or 2)
- Activities home pages (x 4)
- Activity Catalog (Indesign for paper version)
Nice to have
• Integration of Design for our consulting and training catalog will be interesting.

Livechat design (the one of Pixelharbor.com is good)
Should not have
• Only psd

Not html

```html
<!DOCTYPE html>
<html lang="en">
<head>
<meta charset="utf-8">
<title>Kelp Strand – Home</title>
<link rel="stylesheet" href="https://fonts.googleapis.com/css2?family=Raleway:wght@300;500;600&family=Open+Sans:wght@600;700&family=Questrial&family=Arimo:ital,wght@0,400;0,700;1,400;1,700&display=swap">
<style>
:root{
  --nav:#5d5868;
  --ink:#3a3a3a;
  --orange:#d8940f;
  --gold-top:#ffd35a;
  --gold-bot:#e8a312;
  --lime-top:#dbe41f;
  --lime-bot:#a8b600;
  --olive:#a9ae00;
  --card-line:#dcdcdc;
  --white:#ffffff;
}
*{box-sizing:border-box;margin:0;padding:0}
html,body{width:1200px;height:881px;overflow:hidden}
body{position:relative;background:var(--white);font-family:'Arimo',Arial,sans-serif;color:var(--ink)}
.abs{position:absolute}

.header-band{left:0;top:0;width:1200px;height:346px;background:linear-gradient(#fff 0,#fff 140px,#e4e4e6 346px);border-bottom:1px solid #d6d6d8}

.brand{left:104px;top:24px;width:190px;height:142px;display:flex;align-items:center;gap:10px}
.brand-dot{width:150px;height:150px;border-radius:50%;background:radial-gradient(circle at 40% 40%,#eef27a,#c9d51d);display:flex;align-items:center;justify-content:center;font-family:'Open Sans',sans-serif;font-weight:700;font-size:24px;color:#4a4656;text-align:center;line-height:1.1}

.field{height:28px;border:1px solid #cfcfcf;border-radius:3px;background:#fff;font-size:12px;color:#9a9a9a;padding:7px 10px}
.login-btn{left:830px;top:22px;width:86px;height:28px;border-radius:3px;background:linear-gradient(#ffd24d,#efa81a);border:1px solid #d89a10;font-family:'Open Sans',sans-serif;font-weight:700;font-size:15px;color:#333;text-align:center;line-height:26px}
.lang{left:927px;top:21px;width:160px;height:29px;border:1px solid #d8d8d8;border-radius:3px;background:linear-gradient(#fff,#ececec);font-size:13px;color:#333;padding:6px 0 0 44px}
.flag{left:12px;top:7px;width:22px;height:14px;background:linear-gradient(90deg,#1d3f9e 33%,#fff 33% 66%,#e02a2a 66%)}
.lang-arrow{right:4px;top:6px;width:16px;height:16px;background:#8a8a8a;border:1px solid #666}

.main-nav{left:284px;top:71px;width:806px;height:49px;background:linear-gradient(#6a6575,var(--nav));border-radius:6px;border:1px solid #4a4654}
.main-nav a{position:absolute;top:13px;font-family:'Open Sans',sans-serif;font-weight:700;font-size:16px;color:#fff;text-decoration:none}
.nav-sep{top:12px;width:1px;height:24px;background:#837e8d}

.activity{top:208px;width:230px;height:85px;border-radius:8px;border:1px solid #c9cc5a;background:linear-gradient(var(--lime-top),var(--lime-bot));box-shadow:0 10px 8px -8px rgba(0,0,0,.25);text-align:center}
.activity.is-active{background:linear-gradient(var(--gold-top),var(--gold-bot));border-color:#e2b64a}
.activity h3{font-family:'Questrial',sans-serif;font-size:28px;color:#2f2f2f;margin-top:8px;font-weight:700;letter-spacing:.5px}
.activity p{font-size:13px;color:#fff;line-height:16px;margin-top:2px}

.hero{left:101px;top:366px;width:998px;height:170px;border:2px solid #d6d6d6;border-radius:4px;overflow:hidden;background:linear-gradient(90deg,#b3b800 0,#d4dc10 45%,#b7bc00 70%)}
.hero-photo{right:0;top:0;width:280px;height:170px;background:linear-gradient(100deg,#e8ece4,#f2f2f2 60%,#dcdcdc);clip-path:polygon(25% 0,100% 0,100% 100%,0 100%)}
.hero-line1{left:50px;top:16px;font-family:'Raleway',sans-serif;font-weight:300;font-size:34px;color:#fff}
.hero-line2{left:50px;top:50px;font-family:'Raleway',sans-serif;font-weight:600;font-size:57px;color:#3c3c3c}
.hero-line3{left:238px;top:112px;font-family:'Raleway',sans-serif;font-weight:300;font-size:34px;color:#fff}
.hero-btn{left:510px;top:116px;width:180px;height:38px;background:#f0b32a;border:2px solid #f8d470;font-family:'Open Sans',sans-serif;font-weight:700;font-size:21px;color:#3a3a3a;text-align:center;line-height:33px}

.card{top:570px;width:231px;height:206px;border:1px solid var(--card-line);border-radius:5px;background:linear-gradient(#fff,#ececec)}
.card h2{position:absolute;left:20px;top:12px;font-family:'Raleway',sans-serif;font-weight:500;font-size:24px;color:var(--orange)}
.news-list{position:absolute;left:18px;top:52px;list-style:none}
.news-list li{font-size:13px;font-weight:700;font-style:italic;color:#333;height:24px}
.news-list li::before{content:"•";color:var(--olive);font-style:normal;margin-right:9px}
.card-text{position:absolute;left:19px;top:52px;width:200px;font-size:12.5px;line-height:18px;color:#333}
.read-more{position:absolute;left:124px;top:173px;width:88px;height:21px;background:linear-gradient(#b8c000,#97a000);border-radius:3px;font-size:12px;font-weight:700;font-style:italic;color:#fff;text-align:center;line-height:21px}
.partner-frame{position:absolute;left:34px;top:54px;width:166px;height:106px;border:3px solid #ddd;background:#fff;display:flex;align-items:center;justify-content:center}
.partner-badge{width:92px;height:92px;border-radius:50%;background:radial-gradient(circle at 40% 40%,#eef27a,#c9d51d)}
.news-intro{position:absolute;left:15px;top:50px;width:210px;font-size:12.5px;font-style:italic;line-height:18px;color:#333}
.mail{position:absolute;left:14px;top:92px;width:198px;height:33px;border:1px solid #d5d5d5;border-radius:4px;background:#fff;font-size:12px;font-style:italic;color:#aaa;padding:9px 10px}
.subscribe{position:absolute;right:3px;top:3px;width:66px;height:25px;border-radius:4px;background:linear-gradient(#c6cc00,#a3ab00);color:#fff;font-size:12px;font-weight:700;font-style:italic;text-align:center;line-height:25px}
.social{position:absolute;top:142px;width:42px;height:42px;border-radius:50%;background:radial-gradient(circle at 40% 35%,#fff,#bdbdbd);box-shadow:0 2px 3px rgba(0,0,0,.3)}

.site-footer{left:0;top:821px;width:1200px;height:60px;background:var(--nav);text-align:center;font-size:14px;color:#fff;line-height:60px;word-spacing:2px}
.site-footer span{margin:0 14px}
</style>
</head>
<body>
<div class="abs header-band"></div>

<div class="abs brand"><div class="brand-dot">Kelp<br>Strand</div></div>

<div class="abs field" style="left:550px;top:22px;width:129px">Username</div>
<div class="abs field" style="left:690px;top:22px;width:129px;color:#888;font-size:15px;padding-top:3px;letter-spacing:1px">•••••••</div>
<div class="abs login-btn">Login</div>
<div class="abs lang"><span class="abs flag"></span>French<span class="abs lang-arrow"></span></div>

<nav class="abs main-nav">
  <a style="left:35px">Accueil</a><span class="abs nav-sep" style="left:125px"></span>
  <a style="left:162px">Kelp Strand</a><span class="abs nav-sep" style="left:316px"></span>
  <a style="left:349px">Metiers</a><span class="abs nav-sep" style="left:443px"></span>
  <a style="left:475px">Non Referenced</a><span class="abs nav-sep" style="left:641px"></span>
  <a style="left:669px">Contact</a>
</nav>

<div class="abs activity is-active" style="left:112px"><h3>Community</h3><p>simply dummy of the printing<br>and typesetting industry.</p></div>
<div class="abs activity" style="left:362px"><h3>Consulting</h3><p>simply dummy of the printing<br>and typesetting industry.</p></div>
<div class="abs activity" style="left:612px"><h3>Traning</h3><p>simply dummy of the printing<br>and typesetting industry.</p></div>
<div class="abs activity" style="left:860px"><h3>Trovanorm</h3><p>simply dummy of the printing<br>and typesetting industry.</p></div>

<section class="abs hero">
  <div class="abs hero-photo" role="img" aria-label="Businessman pushing up a rising bar chart with an orange growth arrow"></div>
  <div class="abs hero-line1">Focus on your core</div>
  <div class="abs hero-line2">business &amp; call</div>
  <div class="abs hero-line3">a land experts.</div>
  <div class="abs hero-btn">More Details..</div>
</section>

<div class="abs card" style="left:103px">
  <h2>Actualites</h2>
  <ul class="news-list">
    <li>Beyond cost reduction</li><li>Purchasing have role</li><li>Beyond cost reduction</li>
    <li>Purchasing have &nbsp;role</li><li>Beyond cost reduction</li><li>Purchasing have &nbsp;role</li>
  </ul>
</div>

<div class="abs card" style="left:357px">
  <h2>Kelp strand</h2>
  <p class="card-text">simply dummy text of the printing and typesetting industry. Lorem standard dummy text ever since the 1500s, when an unknown printer took a galley of type and make a type specimen book.</p>
  <div class="read-more">Read More »</div>
</div>

<div class="abs card" style="left:611px">
  <h2>Partenariats</h2>
  <svg class="abs" style="left:10px;top:92px" width="16" height="26" viewBox="0 0 16 26"><path d="M13 2 3 13l10 11" fill="none" stroke="#333" stroke-width="3"/></svg>
  <div class="partner-frame"><div class="partner-badge"></div></div>
  <svg class="abs" style="left:207px;top:92px" width="16" height="26" viewBox="0 0 16 26"><path d="m3 2 10 11L3 24" fill="none" stroke="#333" stroke-width="3"/></svg>
</div>

<div class="abs card" style="left:865px">
  <h2 style="left:15px;top:14px">Newsletter</h2>
  <p class="news-intro">Lorem Ipsum is simply dummy text of the printing typesetting industry.</p>
  <div class="mail">Insert Mail<span class="subscribe">Subscribe</span></div>
  <span class="social" style="left:16px"></span>
  <span class="social" style="left:66px"></span>
  <span class="social" style="left:118px"></span>
  <span class="social" style="left:168px"></span>
</div>

<footer class="abs site-footer">
  <span>Mentions Legales</span>|<span>Plan du site</span>|<span>Kelp strand</span>|<span>Blog</span>
</footer>
</body>
</html>
```